Visitenkarten für Urologisches Zentrum Lindenhof
Zielgruppe
Urologisches Zentrum Lindenhof / Vasektomie-Zentrum Lindenhof
Aufgabenstellung
Bitte an der alten Vorlage orientieren. Die 1. Seite (Aussenseite der Klappkarte) ist in Ordnung.
2. Seite (Innenseite der Klappkarte): Hier ggf. eine besser lesbare Schrift.
Adresse: Dr. med. FELIX BRANDT &
Dr. med. MARTIN OSWALD
Birkenweg 17
68161 Mannheim
Fon: unverändert, jedoch bitte etwas übersichtlicher
Fax: unverändert, jedoch bitte etwas übersichtlicher
E-Mail: unverändert, jedoch bitte etwas übersichtlicher
Web: unverändert, jedoch bitte etwas übersichtlicher
Öffnungszeiten: Mo,Di: 08:00 - 12:00 Uhr
14:00 - 16:00 Uhr
Mi: 08:00 - 12:00 Uhr
Do,Fr: 08.00 - 12:00 Uhr
Es sollte noch folgender Text eingefügt werden: Wußten Sie schon? Sie können bei uns Termine über www.terminofix.de
vereinbaren.
Bitte machen Sie uns einige dynamischere Gestaltungsvorschläge. Die Karte sollte in weiß gehalten werden. Keine Glanzbeschichtung und etwas kräftigeres, hochwertiges Papier.
Ich freue mich auf Ihre Vorschläge.

```html
<!DOCTYPE html>
<html lang="de">
<head>
<meta charset="utf-8">
<title>Visitenkarte – Urologisches Zentrum Lindenhof</title>
<link href="https://fonts.googleapis.com/css2?family=Barlow:ital,wght@1,700;1,800&family=Figtree:wght@600;700&family=Arimo&display=swap" rel="stylesheet">
<style>
  :root {
    --paper: #ffffff;
    --ink: #111111;
    --accent: #8bb02a;
    --rule: #9a9a9a;
  }
  html, body { margin: 0; padding: 0; overflow: hidden; background: var(--paper); }
  .card {
    position: relative;
    width: 1200px;
    height: 388px;
    background: var(--paper);
    overflow: hidden;
    color: var(--ink);
  }
  .fold { position: absolute; left: 602px; top: 0; width: 1px; height: 388px; background: var(--rule); }

  .panel { position: absolute; top: 0; height: 388px; }
  .panel--contact { left: 0; width: 602px; }
  .panel--hours { left: 603px; width: 597px; }

  .line {
    position: absolute;
    left: 0; right: 0;
    margin: 0;
    text-align: center;
    line-height: 1;
    white-space: nowrap;
  }
  .headline {
    font-family: "Barlow", sans-serif;
    font-style: italic;
    font-weight: 800;
    font-size: 45px;
    letter-spacing: -0.4px;
    color: var(--accent);
  }
  .contact {
    font-family: "Figtree", sans-serif;
    font-weight: 700;
    font-size: 27px;
  }
  .label {
    font-size: 12px;
    font-weight: 700;
    letter-spacing: 0.5px;
    text-transform: uppercase;
    color: var(--accent);
    margin-right: 7px;
    vertical-align: 3px;
  }

  .hours {
    position: absolute;
    left: 118px;
    top: 150px;
    width: 362px;
    display: grid;
    grid-template-columns: 112px 1fr;
    row-gap: 8px;
    font-family: "Figtree", sans-serif;
    font-weight: 700;
    font-size: 26px;
    line-height: 1;
  }
  .hours__day { grid-column: 1; }
  .hours__time { grid-column: 2; text-align: right; }
  .hours__gap { grid-column: 1 / 3; height: 2px; }

  .hint {
    font-family: "Arimo", sans-serif;
    font-size: 11.5px;
    color: var(--ink);
  }
  .hint a { color: var(--accent); text-decoration: none; }
</style>
</head>
<body>
<div class="card">
  <section class="panel panel--contact">
    <h1 class="line headline" style="top:52px">Dr. med. Felix Brandt &amp;</h1>
    <h1 class="line headline" style="top:88px">Dr. med. Martin Oswald</h1>

    <p class="line contact" style="top:155px">Birkenweg 17</p>
    <p class="line contact" style="top:184px">68161 Mannheim</p>

    <p class="line contact" style="top:241px"><span class="label">Fon</span>0621 482 17 | 0621 739 204 58</p>
    <p class="line contact" style="top:270px"><span class="label">Fax</span>0621 482 17</p>
    <p class="line contact" style="top:299px"><span class="label">E-Mail</span>praxis@brandt-oswald.de</p>
    <p class="line contact" style="top:328px"><span class="label">Web</span>www.brandt-oswald.de</p>
  </section>

  <div class="fold"></div>

  <section class="panel panel--hours">
    <h2 class="line headline" style="top:53px; font-size:47px;">ÖFFNUNGSZEITEN</h2>

    <div class="hours">
      <span class="hours__day">Mo, Di</span><span class="hours__time">08:00 – 12:00 Uhr</span>
      <span class="hours__day"></span><span class="hours__time">14:00 – 16:00 Uhr</span>
      <span class="hours__gap"></span>
      <span class="hours__day">Mi</span><span class="hours__time">08:00 – 12:00 Uhr</span>
      <span class="hours__gap"></span>
      <span class="hours__day">Do, Fr</span><span class="hours__time">08:00 – 12:00 Uhr</span>
    </div>

    <p class="line hint" style="top:349px">Wußten Sie schon? Sie können bei uns Termine über <a href="#">www.terminofix.de</a> vereinbaren.</p>
  </section>
</div>
</body>
</html>
```